Unique and original Business Card for Financial Services Business

I have moved premises and need to change the detail on my business card so thought now is a good time for a re-design. Looking for something professional and modern with colours to fit in with out logo. Like the idea of foil or embossing if that works but not a must have but I do want something that stands out and that I could not design myself.

Once business card is designed I will also be looking to get letterhead and flyers done but want the business card concept in place first.

The majority of designs I am receiving are generic and template based. I am looking for something unique and original. We have some great design elements in our logo, think outside the box and show me something that stands out from the crowd.

Target Market(s)

Business Professionals

Industry/Entity Type

Finance

Contact Information for Business Card

Name: Delia Norwood Phone 0473 958 162 Address PO Box 8617 Mossvale NSW 2389 Email info@steadyharbourfinancialservices.com.au website www.steadyharbourfinancialservices.com.au

Font styles to use
Other font styles liked:
• Ralway

Requirements
Should not have
• No black backgrounds please

```html
<!DOCTYPE html>
<html lang="en">
<head>
<meta charset="utf-8">
<title>Steady Harbour Financial Services – Business Card</title>
<link rel="stylesheet" href="https://fonts.googleapis.com/css2?family=Open+Sans:wght@400;600;700&display=swap">
<style>
  :root {
    --stage: #000000;
    --card: #27272c;
    --pattern-dark: #141416;
    --pattern-mid: #2c2c31;
    --pattern-light: #707075;
    --bird-edge: #55555a;
    --bird-body: #0f0f11;
    --teal: #0b7f8a;
    --teal-bright: #17a3ad;
    --white: #ffffff;
    --text: #f2f2f2;
  }
  * { box-sizing: border-box; margin: 0; padding: 0; }
  html, body {
    width: 1200px; height: 1200px; overflow: hidden;
    background: var(--stage);
    font-family: "Open Sans", Arial, sans-serif;
  }
  .stage { position: relative; width: 1200px; height: 1200px; }
  .card {
    position: absolute; left: 219px; width: 753px; height: 431px;
    background: var(--card); overflow: hidden;
  }
  .card--front { top: 144px; }
  .card--back { top: 620px; }

  .bird-pattern {
    position: absolute; inset: 0;
    background: linear-gradient(205deg, var(--pattern-light) 0%, #4a4a4f 22%, var(--pattern-mid) 48%, var(--pattern-dark) 100%);
  }

  .wordmark { position: absolute; color: var(--white); font-weight: 600; }
  .wordmark__row { display: flex; align-items: center; gap: 10px; }
  .wordmark__square { width: 16px; height: 16px; background: var(--teal); flex: none; }
  .wordmark__name { letter-spacing: -0.5px; line-height: 1; white-space: nowrap; }
  .wordmark__tag { font-weight: 400; line-height: 1; white-space: nowrap; margin-top: 6px; }

  .card--front .wordmark { right: 38px; top: 356px; text-align: right; }
  .card--front .wordmark__name { font-size: 32px; }
  .card--front .wordmark__tag { font-size: 15px; letter-spacing: 0.5em; margin-right: -0.5em; }

  .card--back .wordmark { left: 25px; top: 133px; }
  .card--back .wordmark__name { font-size: 36px; }
  .card--back .wordmark__tag { font-size: 19px; letter-spacing: 0.52em; margin-left: 26px; }

  .holder-name {
    position: absolute; top: 24px; right: 0;
    display: flex; align-items: center; gap: 8px;
    font-weight: 700; font-size: 40px; line-height: 1;
  }
  .holder-name__first { color: var(--teal); }
  .holder-name__last { color: var(--white); }
  .holder-name__bar {
    width: 21px; height: 42px;
    background: linear-gradient(90deg, var(--teal), var(--teal-bright));
  }

  .bird-art {
    position: absolute; left: 472px; top: 87px; width: 281px; height: 344px;
    border-radius: 55% 45% 40% 60% / 40% 35% 65% 60%;
    background: linear-gradient(160deg, var(--bird-edge) 0%, #2e2e32 30%, var(--bird-body) 70%, #1a1a1d 100%);
    box-shadow: 0 0 18px rgba(0,0,0,0.5);
  }

  .address {
    position: absolute; left: 27px; top: 262px;
    color: var(--text); font-size: 19.5px; line-height: 27px;
  }
  .contact-list {
    position: absolute; left: 25px; top: 326px; list-style: none;
    color: var(--text); font-size: 19.5px;
  }
  .contact-list li { display: flex; align-items: center; gap: 14px; height: 27px; }
  .contact-list svg { width: 18px; height: 18px; flex: none; }
</style>
</head>
<body>
<main class="stage">
  <section class="card card--front" aria-label="Card front">
    <div class="bird-pattern" role="img" aria-label="Embossed repeating hummingbird pattern, dark at lower left fading to light grey at upper right"></div>
    <div class="wordmark">
      <div class="wordmark__row" style="justify-content:flex-end">
        <span class="wordmark__square"></span>
        <span class="wordmark__name">STEADY HARBOUR</span>
      </div>
      <div class="wordmark__tag">Financial Services</div>
    </div>
  </section>

  <section class="card card--back" aria-label="Card back">
    <div class="wordmark">
      <div class="wordmark__row">
        <span class="wordmark__square"></span>
        <span class="wordmark__name">STEADY HARBOUR</span>
      </div>
      <div class="wordmark__tag">Financial Services</div>
    </div>

    <h1 class="holder-name">
      <span class="holder-name__first">Delia</span>
      <span class="holder-name__last">Norwood</span>
      <span class="holder-name__bar"></span>
    </h1>

    <div class="bird-art" role="img" aria-label="Large embossed dark hummingbird silhouette in flight"></div>

    <p class="address">PO Box 8617 Mossvale<br>NSW 2389</p>

    <ul class="contact-list">
      <li>
        <svg viewBox="0 0 24 24" fill="none" stroke="var(--teal)" stroke-width="2.4" stroke-linecap="round" stroke-linejoin="round"><path d="M5 3h4l2 5-3 2a12 12 0 0 0 6 6l2-3 5 2v4a2 2 0 0 1-2 2A18 18 0 0 1 3 5a2 2 0 0 1 2-2z"/></svg>
        <span>0473 958 162</span>
      </li>
      <li>
        <svg viewBox="0 0 24 24" fill="none" stroke="var(--teal)" stroke-width="2.4" stroke-linejoin="round"><rect x="2" y="5" width="20" height="14" rx="1"/><path d="M2 6l10 7 10-7"/></svg>
        <span>info@steadyharbourfinancialservices.com.au</span>
      </li>
      <li>
        <svg viewBox="0 0 24 24" fill="none" stroke="var(--teal)" stroke-width="2.2"><circle cx="12" cy="12" r="10"/><path d="M2 12h20M12 2c3 3 3 17 0 20M12 2c-3 3-3 17 0 20"/></svg>
        <span>www.steadyharbourfinancialservices.com.au</span>
      </li>
    </ul>
  </section>
</main>
</body>
</html>
```